Es wurden alle Wünsche immer rasch und professionell umgesetzt. Wir sind rundum zufrieden. Vielen Dank :)
Wir sind ein junges Fotografen-Paar, und wollen heuer neu durchstarten mit Kinder- und Neugeborenen Fotografie. Unsere Zielgruppe sind vor allem schwangere Frauen, die frühzeitig ein Newborn-Shooting oder vorab ein Schwangerschafts-Shooting buchen möchten. Wir sind auf der Suche nach einem minimalistischen Flyer zum Auslegen in diversen Einrichtungen, und einer dazu passenden Visitenkarte.
Wir haben kein Logo, möchten aber auch nichts aufwendiges. Es darf auch ein passendes fertiges Stock-Logo sein.
Wir lieben den BoHo Stil, und fotografieren auch fast ausschließlich in diesem. Dementsprechend stellen wir uns unseren Flyer bzw unsere Visitenkarte minimalistisch vor. Da es um Kinder und Babys geht, ziehen wir die Farbe Altrosa/Rosé vor, eventuell als Akzentfarbe, oder auch als Hintergrundfarbe.
Der Flyer zum Auslegen in Tagesstätten oder zB im Krankenhaus stellen wir uns quadratisch vor (einfacher Flyer/Doppelseitig).
Die Visitenkarte eventuell Hochformat, jedoch sind wir hier total offen. Meine Partnerin meint ein 'BOHO-Regenbogen' wäre bestimmt sehr lieb, jedoch soll dies keine Voraussetzung sein.
Auf der Vorderseite soll unser Logo und ein Foto sein (Baby/Newborn).
Auf der Rückseite mindestens 3-4 unserer Bilder, und einen kurzen Text plus Kontaktdaten.

```html
<!DOCTYPE html>
<html lang="de">
<head>
<meta charset="utf-8">
<title>Lichtnest Atelier – Flyer und Visitenkarten</title>
<link rel="stylesheet" href="https://fonts.googleapis.com/css2?family=Inter:wght@300;400&family=Kalam:wght@300;400&display=swap">
<style>
  :root {
    --backdrop: #adadad;
    --paper: #ffffff;
    --rose: #f0a3ad;
    --rose-line: #f2b3bb;
    --rose-deep: #c95a6e;
    --blush: #f1d2d7;
    --ink-soft: #8c8c8c;
    --tan: #c98a4e;
  }
  * { box-sizing: border-box; margin: 0; padding: 0; }
  html, body { width: 1200px; height: 934px; overflow: hidden; }
  body { background: var(--backdrop); font-family: "Inter", Arial, sans-serif; position: relative; }

  .card { position: absolute; background: var(--paper); }
  .flyer { width: 495px; height: 495px; }
  .flyer--baby { left: 77px; top: 55px; }
  .flyer--kids { left: 610px; top: 107px; }
  .bizcard { width: 316px; height: 212px; }
  .bizcard--front { left: 264px; top: 651px; }
  .bizcard--back { left: 640px; top: 679px; background: var(--blush); }

  .brand-rule { position: absolute; height: 1px; background: var(--rose-line); }
  .brand-dot { position: absolute; border-radius: 50%; background: var(--tan); }
  .brand-name { position: absolute; left: 0; right: 0; text-align: center; color: var(--rose); font-weight: 300; letter-spacing: .5px; }

  .flyer .brand-rule { top: 47px; width: 155px; }
  .flyer .brand-rule.left { left: 57px; }
  .flyer .brand-rule.right { right: 57px; }
  .flyer .brand-dot { top: 35px; left: 235px; width: 24px; height: 24px; }
  .flyer .brand-name { top: 70px; font-size: 19px; }

  .photo { position: absolute; }
  .tagline { position: absolute; left: 0; right: 0; text-align: center; font-family: "Kalam", "Comic Sans MS", cursive; font-weight: 300; color: var(--ink-soft); }
  .contact { position: absolute; left: 62px; right: 58px; top: 440px; display: flex; justify-content: space-between; color: var(--rose); font-size: 15px; font-weight: 300; }

  .flyer--baby .tagline { top: 385px; font-size: 36px; }
  .flyer--kids .tagline { top: 330px; font-size: 33px; line-height: 1.2; }

  .bizcard--front .brand-rule.top { top: 45px; width: 100px; }
  .bizcard--front .brand-rule.left { left: 42px; }
  .bizcard--front .brand-rule.right { right: 44px; }
  .bizcard--front .brand-dot { top: 36px; left: 150px; width: 16px; height: 16px; }
  .bizcard--front .brand-name { top: 62px; font-size: 13px; color: var(--rose-deep); }
  .bizcard--front .brand-rule.under { top: 84px; left: 44px; right: 44px; }
  .bizcard--front .tagline { top: 100px; font-size: 16px; line-height: 1.5; }
  .bizcard--front .contact { left: 28px; right: 24px; top: 178px; font-size: 11px; }

  .bizcard--back .brand-name { top: 68px; font-size: 14px; color: var(--rose-deep); }
  .bizcard--back .brand-rule.under { top: 92px; left: 46px; right: 46px; background: #e28e9c; }
  .bizcard--back .tagline { top: 108px; font-size: 27px; color: #888; }
</style>
</head>
<body>

<section class="card flyer flyer--baby">
  <span class="brand-rule left"></span><span class="brand-dot"></span><span class="brand-rule right"></span>
  <h2 class="brand-name">LICHTNEST ATELIER</h2>
  <div class="photo" role="img" aria-label="Neugeborenes schlafend auf altrosa Strickdecke mit Haarband" style="left:60px;top:125px;width:246px;height:245px;background:linear-gradient(135deg,#5a3f3a,#9b6e6e 55%,#b58a92);"></div>
  <div class="photo" role="img" aria-label="Neugeborenes in blauem Tuch auf blauem Fell" style="left:311px;top:125px;width:120px;height:118px;background:linear-gradient(160deg,#35505f,#4f7386);"></div>
  <div class="photo" role="img" aria-label="Neugeborenes mit Strickmütze auf den Händen liegend" style="left:311px;top:248px;width:120px;height:120px;background:linear-gradient(160deg,#b5aca3,#8a7a6c);"></div>
  <p class="tagline">Babyfotografie</p>
  <div class="contact"><span>www.lichtnest.de</span><span>Tel: 01765550123</span></div>
</section>

<section class="card flyer flyer--kids">
  <span class="brand-rule left"></span><span class="brand-dot"></span><span class="brand-rule right"></span>
  <h2 class="brand-name">LICHTNEST ATELIER</h2>
  <div class="photo" role="img" aria-label="Kleinkind mit Köfferchen auf einem Feldweg im Herbstlicht" style="left:60px;top:125px;width:118px;height:178px;background:linear-gradient(170deg,#c9b98a,#6f6a45 45%,#7a6a55);"></div>
  <div class="photo" role="img" aria-label="Drei Geschwister Hand in Hand auf einem Weg" style="left:182px;top:125px;width:124px;height:87px;background:linear-gradient(170deg,#d2c49a,#6d7047 60%,#8a7f64);"></div>
  <div class="photo" role="img" aria-label="Zwei Kinder sitzen im Gras bei Sonnenuntergang" style="left:182px;top:216px;width:124px;height:87px;background:linear-gradient(170deg,#e0b46a,#8a7a3a 50%,#5f5a30);"></div>
  <div class="photo" role="img" aria-label="Mädchen mit Haarband in herbstlicher Wiese" style="left:310px;top:125px;width:122px;height:178px;background:linear-gradient(170deg,#d9c58f,#8e8045 50%,#58603a);"></div>
  <p class="tagline">Fotografie für Kinder<br>und Neugeborene</p>
  <div class="contact"><span>www.lichtnest.de</span><span>Tel: 01765550123</span></div>
</section>

<section class="card bizcard bizcard--front">
  <span class="brand-rule top left"></span><span class="brand-dot"></span><span class="brand-rule top right"></span>
  <h3 class="brand-name">LICHTNEST ATELIER</h3>
  <span class="brand-rule under"></span>
  <p class="tagline">Fotografie für Kinder<br>und Neugeborene</p>
  <div class="contact"><span>www.lichtnest.de</span><span>Tel: 01765550987</span></div>
</section>

<section class="card bizcard bizcard--back">
  <h3 class="brand-name">LICHTNEST ATELIER</h3>
  <span class="brand-rule under"></span>
  <p class="tagline">Babyfotografie</p>
</section>

</body>
</html>
```